Verdant Loop Advisors, LLC

I am looking for a simple, clear layout with my logo prominent and embossed, on the best quality card stock available. I would like the business name and phone number included on the card as well......I dont want my name anywhere on the card and I would like my logo embossed on the card......something simple with a white back......open to designs as long as they go along with recycling symbols and green type stuff.....The address, website, cell number, fax number, and email are listed below

5374 Tillbury Fenwood Road
Fenmarsh, MD 20999

c. 240.555.0143 f. 240.555.0187
e. sales@verdantloopadvisors.example
w. www.verdantloopadvisors.example

Industry/Entity Type

Recycling

```html
<!DOCTYPE html>
<html lang="en">
<head>
<meta charset="utf-8">
<title>Verdant Loop Advisors, LLC — Business Card</title>
<link rel="stylesheet" href="https://fonts.googleapis.com/css2?family=PT+Sans:ital,wght@0,400;0,700;1,400&display=swap">
<style>
  :root {
    --card-bg: #e8e8e8;
    --brand-green: #0f6e2f;
    --brand-green-light: #2f7d42;
    --ink: #111111;
    --text: #2a2a2a;
    --label-green: #2e7a3c;
  }
  * { margin: 0; padding: 0; box-sizing: border-box; }
  html, body {
    width: 1200px;
    height: 720px;
    overflow: hidden;
    background: var(--card-bg);
  }
  .card {
    position: relative;
    width: 1200px;
    height: 720px;
    background: var(--card-bg);
    font-family: "PT Sans", Arial, sans-serif;
    color: var(--text);
  }
  .brand-mark {
    position: absolute;
    left: 50%;
    top: 72px;
    width: 326px;
    height: 326px;
    transform: translateX(-50%);
    border-radius: 50%;
    background: radial-gradient(circle at 40% 25%, var(--brand-green-light), var(--brand-green) 70%);
  }
  .brand-name {
    position: absolute;
    left: 0;
    right: 0;
    top: 458px;
    text-align: center;
    font-size: 42px;
    line-height: 60px;
    font-weight: 700;
    letter-spacing: 1px;
    text-transform: uppercase;
    color: var(--ink);
  }
  .contact {
    position: absolute;
    left: 0;
    right: 0;
    top: 556px;
    text-align: center;
    font-size: 28px;
    line-height: 37px;
    list-style: none;
  }
  .contact li { white-space: nowrap; }
  .contact-item + .contact-item { margin-left: 14px; }
  .contact-label {
    font-style: italic;
    color: var(--label-green);
    margin-right: 10px;
  }
</style>
</head>
<body>
  <main class="card">
    <div class="brand-mark" aria-hidden="true"></div>
    <h1 class="brand-name">Verdant Loop Advisors, LLC</h1>
    <ul class="contact">
      <li><span class="contact-item"><span class="contact-label">a</span>5374 Tillbury Fenwood Road, Fenmarsh, MD 20999</span></li>
      <li>
        <span class="contact-item"><span class="contact-label">c</span>240.555.0143</span>
        <span class="contact-item"><span class="contact-label">f</span>240.555.0187</span>
        <span class="contact-item"><span class="contact-label">e</span>sales@verdantloopadvisors.example</span>
      </li>
      <li><span class="contact-item"><span class="contact-label">w</span>www.verdantloopadvisors.example</span></li>
    </ul>
  </main>
</body>
</html>
```